We need a letterhead design for a new international company based in Luanda, Angola called "Solmarin Corporation". Solmarin Corporation is a multiservice private company. We provides services for the following sectors: Oil & Gas industry, Government, and the Public.

Target Market(s)

Board of directors of the following sectors: Oil & Gas industry, Government, and the Public.

Industry/Entity Type

Government

Requirements
Must have
• Solmarin Corporation logo

```html
<!DOCTYPE html>
<html lang="en">
<head>
<meta charset="utf-8">
<title>Solmarin Corporation Letterhead</title>
<link rel="stylesheet" href="https://fonts.googleapis.com/css2?family=Exo+2:wght@400;500&display=swap">
<style>
  :root {
    --paper: #ffffff;
    --ink: #1a1a1a;
    --brand-red: #c8202a;
    --rule: #f2a7b0;
    --watermark-gold: rgba(245, 228, 170, 0.35);
    --watermark-rose: rgba(240, 170, 175, 0.28);
  }
  * { margin: 0; padding: 0; box-sizing: border-box; }
  html, body {
    width: 848px;
    height: 1200px;
    overflow: hidden;
    background: var(--paper);
  }
  .letterhead {
    position: relative;
    width: 848px;
    height: 1200px;
    background: var(--paper);
    font-family: "Exo 2", sans-serif;
    color: var(--ink);
  }
  .brand {
    position: absolute;
    left: 30px;
    top: 62px;
    display: flex;
    align-items: center;
    gap: 18px;
  }
  .brand-mark {
    width: 56px;
    height: 56px;
    border-radius: 50%;
    background: var(--brand-red);
  }
  .brand-name {
    font-size: 30px;
    font-weight: 500;
    line-height: 1;
    letter-spacing: 0.5px;
    color: var(--ink);
  }
  .contact {
    position: absolute;
    right: 32px;
    top: 40px;
    text-align: right;
    font-size: 13px;
    line-height: 16px;
  }
  .contact .address { margin-bottom: 17px; }
  .contact .phones { margin-bottom: 15px; }
  .watermark {
    position: absolute;
    left: 190px;
    top: 370px;
    width: 658px;
    height: 830px;
    background:
      radial-gradient(ellipse 45% 55% at 32% 62%, var(--watermark-gold), transparent 70%),
      radial-gradient(ellipse 40% 55% at 85% 40%, var(--watermark-rose), transparent 70%);
  }
  .footer-rule {
    position: absolute;
    left: 20px;
    right: 21px;
    top: 1163px;
    height: 1px;
    background: var(--rule);
  }
  .board {
    position: absolute;
    left: 0;
    right: 0;
    top: 1168px;
    text-align: center;
    font-size: 13px;
    padding-right: 0;
    transform: translateX(0);
  }
</style>
</head>
<body>
  <div class="letterhead">
    <div class="watermark" role="img" aria-label="Large faint company emblem watermark in pale gold and rose"></div>

    <header class="brand">
      <span class="brand-mark"></span>
      <span class="brand-name">Solmarin Corporation</span>
    </header>

    <address class="contact" style="font-style: normal;">
      <p class="address">Address Line 1, Address Line 2<br>Address Line 3, Address Line 4</p>
      <p class="phones">Telephone:<br>Facsimile:</p>
      <p class="email">Email: address@address</p>
    </address>

    <div class="footer-rule"></div>
    <footer class="board">Board Members: Name Surname | Name Surname | Name Surname | Name Surname</footer>
  </div>
</body>
</html>
```